UK based Drone services needs a pdf / flyer designed.

I am looking to get a flyer advertising what we do. I have added a word document with a little background and what services we offer, please could you add images for each service if possible? We are NPB approved and would like that to be mentioned on the bottom right corner please (logo attached). All our work is carried out with TQX drones, so would ideally like maybe a TQX Halvorn 620 rtk image in there. BrixtonUAV is the name of the company. Please get back to me if you have any questions.

```html
<!DOCTYPE html>
<html lang="en">
<head>
<meta charset="utf-8">
<title>BrixtonUAV – Unmanned Aerial Vehicles Flyer</title>
<link rel="stylesheet" href="https://fonts.googleapis.com/css2?family=Poppins:wght@300;400;500;600;700;800&display=swap">
<style>
  :root{
    --bg-page:#e9e9e9;
    --bg-dark:#1f2022;
    --teal:#4fa8b8;
    --teal-box:#56a8b6;
    --ink-navy:#1d3a4c;
    --ring:#2c3f43;
    --white:#ffffff;
  }
  *{box-sizing:border-box;margin:0;padding:0}
  html,body{width:1200px;height:2400px;overflow:hidden;background:var(--bg-page);font-family:"Poppins",sans-serif}
  .flyer{position:absolute;left:0;top:424px;width:1200px;height:1552px;background:var(--bg-dark);overflow:hidden;color:var(--white)}
  .hero-photo{position:absolute;left:0;top:0;width:1200px;height:640px;
    background:linear-gradient(180deg,#6f777b 0%,#4b5357 35%,#2d3033 70%,var(--bg-dark) 100%)}
  .hero-drone{position:absolute;left:440px;top:60px;width:760px;height:382px;
    background:radial-gradient(ellipse at 55% 45%,#3a3d40 0%,#2a2c2f 55%,rgba(42,44,47,0) 75%)}
  .brand{position:absolute;left:69px;top:150px;font-weight:500;font-size:46px;letter-spacing:1px;color:var(--white)}
  .kicker{position:absolute;left:64px;top:304px;font-weight:300;font-size:47px;letter-spacing:12px;line-height:1}
  .headline{position:absolute;left:62px;top:360px;font-weight:800;line-height:.98;letter-spacing:-1px}
  .headline span{display:block;font-size:104px}
  .headline .accent{color:var(--teal)}
  .headline .plain{color:var(--white);font-size:106px}
  .intro{position:absolute;left:66px;top:680px;width:540px;font-weight:500;font-size:18.5px;line-height:1.22}
  .benefits{position:absolute;left:652px;top:472px;width:494px;list-style:none}
  .benefits li{position:relative;padding:0 0 10px 30px;margin-bottom:12px;font-size:16.8px;line-height:1.2;border-bottom:1.5px dashed var(--teal)}
  .benefits li:last-child{border-bottom:none}
  .benefits svg{position:absolute;left:0;top:4px;width:14px;height:14px}
  .kit-photo{position:absolute;left:81px;top:788px;width:406px;height:376px;border-radius:24px;
    background:radial-gradient(ellipse at 50% 55%,#3b3f44 0%,#2a2d31 55%,rgba(31,32,34,0) 80%)}
  .about{position:absolute;left:485px;top:848px;width:715px;height:250px;background:var(--teal-box);color:var(--ink-navy);
    padding:26px 44px 0 30px;font-weight:500;font-size:16.3px;line-height:1.2}
  .about p+p{margin-top:18px}
  .services-title{position:absolute;left:746px;top:1112px;font-weight:700;font-size:37px;letter-spacing:.5px}
  .services-rule{position:absolute;left:69px;top:1162px;width:670px;border-top:2px dotted #3d5257}
  .services-rule::before{content:"";position:absolute;left:-4px;top:-5px;width:8px;height:8px;border-radius:50%;background:var(--teal)}
  .services{position:absolute;left:0;top:1170px;width:1200px;height:180px}
  .service{position:absolute;width:200px;margin-left:-100px;text-align:center;top:0}
  .service .disc{width:166px;height:166px;margin:0 auto;border-radius:50%;border:9px solid var(--ring)}
  .service .label{margin-top:10px;font-size:20px;line-height:1.12}
  .d1{background:linear-gradient(180deg,#b9c4bd,#5c7a4b)}
  .d2{background:linear-gradient(135deg,#6b7a5c,#a9aa93 50%,#4c5e40)}
  .d3{background:linear-gradient(180deg,#3a3532,#221f1e)}
  .d4{background:linear-gradient(180deg,#b7c8d8,#8da0b2 60%,#3d4f63)}
  .d5{background:linear-gradient(180deg,#d9dfe4,#9aa3ab 60%,#7b6c63)}
  .d6{background:linear-gradient(180deg,#f0f2ee,#b8c08e 55%,#4c6b2c)}
  .contact{position:absolute;left:61px;top:1445px;width:1079px;height:48px;border:2px solid var(--teal);border-radius:24px;display:flex;align-items:center;white-space:nowrap}
  .contact-label{flex:0 0 210px;height:48px;margin:-2px 0 -2px -2px;background:var(--teal-box);border-radius:24px 0 0 24px;color:var(--ink-navy);
    font-weight:700;font-size:23px;display:flex;align-items:center;padding-left:28px}
  .contact-item{flex:0 0 auto;display:flex;align-items:center;gap:6px;font-weight:600;font-size:20px;padding:0 18px;white-space:nowrap}
  .contact-item svg{width:19px;height:19px;flex:0 0 19px}
  .sep{flex:0 0 2px;height:28px;background:var(--white)}
  .web{letter-spacing:2px}
</style>
</head>
<body>
<main class="flyer">
  <div class="hero-photo" role="img" aria-label="Misty snow-covered mountain range under cloud"></div>
  <div class="hero-drone" role="img" aria-label="TQX Halvorn 620 rtk drone in flight with gimbal camera"></div>

  <div class="brand">BrixtonUAV</div>
  <div class="kicker">UNMANNED</div>
  <h1 class="headline">
    <span class="accent">ARIAL</span>
    <span class="accent">VEHICLES</span>
    <span class="plain">(UAV'S)</span>
  </h1>
  <p class="intro">UAV’s are revolutionizing the way industries are able to work. With current advances in technology, drones are opening doors that weren't available before.</p>

  <ul class="benefits">
    <li><svg viewBox="0 0 14 14"><circle cx="7" cy="7" r="6" fill="none" stroke="#4fa8b8" stroke-width="1.3"/><path d="M4 7.2l2 2 4-4.2" fill="none" stroke="#4fa8b8" stroke-width="1.3"/></svg>With the ability to reach difficult and dangerous areas, they remove the human element and change the scope of what's safely possible.</li>
    <li><svg viewBox="0 0 14 14"><circle cx="7" cy="7" r="6" fill="none" stroke="#4fa8b8" stroke-width="1.3"/><path d="M4 7.2l2 2 4-4.2" fill="none" stroke="#4fa8b8" stroke-width="1.3"/></svg>Capturing live Ultra High-Definition footage ofunreachable areas and making working at heights a thing of the past.</li>
    <li><svg viewBox="0 0 14 14"><circle cx="7" cy="7" r="6" fill="none" stroke="#4fa8b8" stroke-width="1.3"/><path d="M4 7.2l2 2 4-4.2" fill="none" stroke="#4fa8b8" stroke-width="1.3"/></svg>Drones are safer, faster, more cost-effective and a highly accurate alternative.</li>
    <li><svg viewBox="0 0 14 14"><circle cx="7" cy="7" r="6" fill="none" stroke="#4fa8b8" stroke-width="1.3"/><path d="M4 7.2l2 2 4-4.2" fill="none" stroke="#4fa8b8" stroke-width="1.3"/></svg>Not only do you have the chance to inspect dangerous areas live, but you also get photographs and/or 4K Ultra HD video footage to review at a later date.</li>
    <li><svg viewBox="0 0 14 14"><circle cx="7" cy="7" r="6" fill="none" stroke="#4fa8b8" stroke-width="1.3"/><path d="M4 7.2l2 2 4-4.2" fill="none" stroke="#4fa8b8" stroke-width="1.3"/></svg>No need to send someone back out to the area to double-check damage, you have it all on record.</li>
  </ul>

  <div class="kit-photo" role="img" aria-label="TQX Halvorn 620 rtk drone above its handheld remote controller with screen"></div>

  <section class="about">
    <p>BrixtonUAV is fully equipped with the latest and most suitable drones for your business or personal needs. From a small roof survey to a full wind turbine site inspection. No project is too small or too large, take advantage of using UAV's now!</p>
    <p>Here at BrixtonUAV, we pride ourselves on being affordable and offering a great product to our clients. We have a comprehensive list of services that we offer to any business or individual across the UK. Our UAV pilots are GVC licensed and have gained Operational Authorization from the NPB allowing us to carry out commercial work in the UK.</p>
  </section>

  <h2 class="services-title">SERVICES WE OFFER</h2>
  <div class="services-rule"></div>

  <div class="services">
    <div class="service" style="left:142px"><div class="disc d1" role="img" aria-label="Compact drone hovering over green field"></div><div class="label">Commercial<br>Inspections</div></div>
    <div class="service" style="left:330px"><div class="disc d2" role="img" aria-label="Aerial survey view of terrain and roads"></div><div class="label">Mapping<br>/Surveys</div></div>
    <div class="service" style="left:520px"><div class="disc d3" role="img" aria-label="Camera drone close-up on dark background"></div><div class="label">Arial<br>Photography<br>/Videography</div></div>
    <div class="service" style="left:705px"><div class="disc d4" role="img" aria-label="Drone inspecting solar panel field"></div><div class="label">Solar Panel<br>Inspections</div></div>
    <div class="service" style="left:889px"><div class="disc d5" role="img" aria-label="Drone flying over town buildings"></div><div class="label">Real Estate<br>/Planning</div></div>
    <div class="service" style="left:1072px"><div class="disc d6" role="img" aria-label="Agricultural drone spraying over crops"></div><div class="label">Agriculture</div></div>
  </div>

  <footer class="contact">
    <div class="contact-label">Contact Us</div>
    <div class="contact-item"><svg viewBox="0 0 20 20"><circle cx="10" cy="10" r="9" fill="none" stroke="#4fa8b8" stroke-width="1.6"/><path d="M6.5 5.5l2 .2.6 2-1.2.9a6 6 0 0 0 3 3l.9-1.2 2 .6.2 2c-.6.8-1.5 1-2.4.8A8 8 0 0 1 5.7 7.9c-.2-.9 0-1.8.8-2.4z" fill="#4fa8b8"/></svg>020 7946 0312</div>
    <div class="sep"></div>
    <div class="contact-item"><svg viewBox="0 0 20 20"><circle cx="10" cy="10" r="9" fill="none" stroke="#4fa8b8" stroke-width="1.6"/><rect x="5.5" y="6.8" width="9" height="6.4" rx="1" fill="none" stroke="#4fa8b8" stroke-width="1.4"/><path d="M5.8 7.2l4.2 3.2 4.2-3.2" fill="none" stroke="#4fa8b8" stroke-width="1.4"/></svg>info@brixtonuav.co.uk</div>
    <div class="sep"></div>
    <div class="contact-item web"><svg viewBox="0 0 20 20"><circle cx="10" cy="10" r="8.5" fill="none" stroke="#4fa8b8" stroke-width="1.6"/><ellipse cx="10" cy="10" rx="3.6" ry="8.5" fill="none" stroke="#4fa8b8" stroke-width="1.3"/><path d="M1.5 10h17M3 5.8h14M3 14.2h14" stroke="#4fa8b8" stroke-width="1.2"/></svg>www.brixtonuav.co.uk</div>
  </footer>
</main>
</body>
</html>
```